Billboard for personal injury chiropractors office

We are a personal injury chiropractor clinic.
I need a Billboard with the company name as the dominating factor. Also a smaller picture or 2 of something creative, like a car accident or an arm in a cast off to the sides.
We Like something Clean and Simple and Eye Catching. Please make the picture Small and Off To The Side. The MAIN FOCUS areas are the… name Varden Chiropractic Clinic
At the top CAR ACCIDENT INJURY?
AND at the bottom our number 418-27-FLEXA.
Dr.Milo R. Varden in bold somewhere with the word chiropractor under the doctors name in a text.

Im open to red lettering on white backgrounds, red on yellow backgrounds and I'm also open to reds blues white and yellow. I'd prefer yellow if used be across the bottom.

I am uploading a very rough draft of what we are after along with a screenshot of the tv commercial showing the yellow

DO NOT USE THE LOGO ON THE COMMERCIAL. I JUST WANT THE NAME TYPED LIKE ON SAMPLE BILLBOARD.

Industry/Entity Type

Chiropractic

Colors
0054AA
0677BA
7BADD7
CADEEF
E8F1F8
FFF300
FFF600
FEFA6F
FFFEC7
FFFEE8
EB3D1F
EC4F4E
F09395
F8D3D4
FCEDEE

Requirements
Must have
• Eye catching ,bold

```html
<!DOCTYPE html>
<html lang="en">
<head>
<meta charset="utf-8">
<title>Varden Chiropractic Clinic – Billboard</title>
<link rel="stylesheet" href="https://fonts.googleapis.com/css2?family=Montserrat:wght@800&family=Poppins:wght@500;600;800&display=swap">
<style>
  :root {
    --mat: #1e1b1c;
    --white: #ffffff;
    --navy: #2e3192;
    --blue: #0677ba;
    --yellow: #fff300;
    --yellow-deep: #f6c210;
    --red: #e52329;
    --ink: #111111;
    --shirt: #1f6cb4;
  }
  html, body {
    margin: 0;
    width: 1200px;
    height: 1200px;
    overflow: hidden;
    background: var(--mat);
  }
  .billboard {
    position: absolute;
    left: 141px;
    top: 354px;
    width: 918px;
    height: 492px;
  }
  .headline, .clinic-name, .clinic-type { font-family: "Montserrat", sans-serif; font-weight: 800; }
  .doctor, .call-label, .phone { font-family: "Poppins", sans-serif; }
</style>
</head>
<body>
<svg class="billboard" viewBox="176 442 1148 615" xmlns="http://www.w3.org/2000/svg">
  <defs>
    <radialGradient id="yellowGlow" cx="0.45" cy="0.55" r="0.7">
      <stop offset="0" stop-color="#fff6a0"/>
      <stop offset="0.45" stop-color="#fff300"/>
      <stop offset="1" stop-color="#f6c210"/>
    </radialGradient>
    <linearGradient id="carTone" x1="0" y1="0" x2="1" y2="1">
      <stop offset="0" stop-color="#d8232c"/>
      <stop offset="1" stop-color="#5a1216"/>
    </linearGradient>
  </defs>

  <!-- background panels -->
  <rect class="panel-white" x="176" y="442" width="1148" height="615" fill="var(--white)"/>
  <polygon class="panel-yellow" points="176,652 1324,588 1324,977 176,977" fill="url(#yellowGlow)"/>
  <circle cx="265" cy="860" r="55" fill="#fffbc0" opacity="0.5"/>
  <circle cx="1060" cy="880" r="60" fill="#fff7a0" opacity="0.45"/>
  <circle cx="790" cy="690" r="70" fill="#fff7a0" opacity="0.35"/>

  <!-- header band -->
  <polygon class="rule-top" points="176,520 660,492 660,502 176,530" fill="var(--blue)"/>
  <polygon class="band-headline" points="258,540 1324,468 1324,568 258,633" fill="var(--navy)"/>
  <polygon class="rule-bottom" points="688,612 1324,574 1324,584 688,622" fill="var(--blue)"/>
  <text class="headline" x="280" y="608" font-size="66" fill="var(--white)" transform="rotate(-3.9 280 608)" textLength="875" lengthAdjust="spacingAndGlyphs">CAR ACCIDENT INJURY</text>
  <text class="headline" x="1182" y="560" font-size="112" fill="var(--red)" transform="rotate(-4 1182 560)">?</text>

  <!-- photo areas -->
  <rect role="img" aria-label="Man in a blue t-shirt with his arm in a white cast" x="1068" y="592" width="256" height="300" fill="var(--shirt)"/>
  <rect role="img" aria-label="Red sports car with a crashed front end" x="1040" y="892" width="284" height="165" fill="url(#carTone)"/>

  <!-- clinic name -->
  <text class="clinic-name" x="650" y="822" text-anchor="middle" font-size="176" textLength="610" lengthAdjust="spacingAndGlyphs" fill="var(--red)">VARDEN</text>
  <text class="clinic-type" x="656" y="914" text-anchor="middle" font-size="58" textLength="616" lengthAdjust="spacingAndGlyphs" fill="var(--ink)">CHIROPRACTIC CLINIC</text>

  <!-- doctor line -->
  <line x1="345" y1="950" x2="528" y2="950" stroke="var(--red)" stroke-width="2"/>
  <line x1="784" y1="950" x2="968" y2="950" stroke="var(--red)" stroke-width="2"/>
  <text class="doctor" x="656" y="958" text-anchor="middle" font-size="23" font-weight="600" fill="#3a1a10">Dr. Milo R. Varden</text>

  <!-- call bar -->
  <rect class="bar-call" x="176" y="977" width="864" height="80" fill="var(--red)"/>
  <text class="call-label" x="198" y="1034" font-size="46" font-weight="500" fill="var(--yellow)">Call Now</text>
  <line x1="430" y1="988" x2="430" y2="1047" stroke="#f6a6a0" stroke-width="4"/>
  <text class="phone" x="462" y="1040" font-size="63" font-weight="800" fill="var(--white)" textLength="556" lengthAdjust="spacingAndGlyphs">418-27-FLEXA.</text>
</svg>
</body>
</html>
```